Copper lark buildworks

Copper lark buildworks is a small construction company.
Who is a licenced builder, Carpenter, joiner,
working on heritage ,new build, speacial projects and sometimes furniture

Industry/Entity Type

Construction

```html
<!DOCTYPE html>
<html lang="en">
<head>
<meta charset="utf-8">
<title>Copper lark buildworks – business card concepts</title>
<link rel="stylesheet" href="https://fonts.googleapis.com/css2?family=Lato:wght@400;700;900&family=Arimo:wght@700&display=swap">
<style>
  :root {
    --page: #e8e5e0;
    --card-white: #ffffff;
    --card-dark: #1c1c1c;
    --ink: #222222;
    --green-bright: #7ed321;
    --green-deep: #2f7d18;
    --green-mid: #4fa825;
    --stripe-grey: #9a9a9a;
    --label-bg: #ffffff;
    --label-ink: #111111;
  }
  * { box-sizing: border-box; margin: 0; padding: 0; }
  html, body { width: 720px; height: 1200px; overflow: hidden; }
  body { background: var(--page); font-family: 'Lato', Arial, sans-serif; position: relative; }

  .concept-label {
    position: absolute; background: var(--label-bg); color: var(--label-ink);
    font-family: 'Arimo', Arial, sans-serif; font-weight: 700; font-size: 24px;
    padding: 4px 10px; left: 50%; transform: translateX(-50%); white-space: nowrap;
  }

  .card { position: absolute; overflow: hidden; box-shadow: 0 6px 14px rgba(0,0,0,.35); background: var(--card-white); }
  .card--split { width: 462px; height: 284px; left: 129px; }
  .card--a { top: 100px; }
  .card--b { top: 480px; }
  .card--c { width: 462px; height: 288px; left: 129px; top: 862px; }

  .panel-light { position: absolute; left: 0; top: 0; width: 232px; height: 100%; background: var(--card-white); }
  .panel-dark { position: absolute; left: 232px; top: 0; right: 0; height: 100%; background: var(--card-dark); color: #fff; }

  .brand { position: absolute; display: flex; align-items: center; gap: 8px; font-weight: 900; color: var(--ink); font-size: 28px; line-height: 1; letter-spacing: -.5px; white-space: nowrap; }
  .brand-dot { width: 13px; height: 13px; border-radius: 50%; background: var(--green-bright); flex: none; }

  .skyline { position: absolute; left: 0; bottom: 0; height: 66px; width: 100%;
    background: linear-gradient(180deg, var(--green-bright) 0%, var(--green-mid) 55%, var(--green-deep) 100%); }

  .person { position: absolute; }
  .person-name { font-size: 25px; font-weight: 400; line-height: 1; white-space: nowrap; }
  .person-name .initial { color: var(--green-bright); }
  .person-role { font-size: 10px; text-align: right; margin-top: 6px; }

  .contacts { position: absolute; list-style: none; }
  .contacts li { display: flex; align-items: center; gap: 10px; font-size: 12px; height: 35px; white-space: nowrap; }
  .contact-icon { width: 18px; height: 18px; flex: none; }

  .services { position: absolute; list-style: none; display: grid; grid-template-columns: auto auto; column-gap: 16px; row-gap: 6px; font-size: 9.5px; }
  .services li { display: flex; align-items: center; gap: 6px; white-space: nowrap; }
  .leaf { width: 9px; height: 7px; flex: none; }

  /* Concept A */
  .card--a .brand { left: 36px; top: 62px; }
  .card--a .services { left: 30px; top: 160px; color: var(--ink); }
  .card--a .person { left: 34px; top: 30px; color: #fff; }
  .card--a .person-role { color: var(--green-bright); }
  .card--a .contacts { left: 34px; top: 112px; }

  /* Concept B */
  .card--b .brand { left: 36px; top: 62px; }
  .card--b .person { left: 30px; top: 160px; color: var(--ink); }
  .card--b .contacts { left: 34px; top: 22px; }
  .card--b .services { left: 22px; top: 226px; color: #fff; }

  /* Concept C */
  .card--c .diagonals { position: absolute; left: 0; top: 0; }
  .card--c .brand { left: 40px; top: 36px; font-size: 22px; }
  .card--c .person { left: 98px; top: 156px; color: var(--ink); }
  .card--c .person-name { color: var(--green-deep); font-size: 22px; }
  .card--c .person-role { font-weight: 700; }
  .card--c .contacts { left: 284px; top: 28px; color: var(--ink); font-weight: 700; }
  .card--c .contacts li { height: 33px; font-size: 11.5px; }
  .card--c .skyline { bottom: 12px; height: 70px; }
  .card--c .footer-strip { position: absolute; left: 0; right: 0; bottom: 0; height: 12px; background: var(--card-dark); }
  .card--c .services { position: static; display: flex; justify-content: center; gap: 18px; color: #fff; font-size: 7.5px; height: 12px; align-items: center; }
</style>
</head>
<body>
<svg width="0" height="0" style="position:absolute" aria-hidden="true">
  <symbol id="i-phone" viewBox="0 0 20 20"><circle cx="10" cy="10" r="8.6" fill="none" stroke="currentColor" stroke-width="1.4"/><path d="M7 5.5l1.6 0 .8 2.2-1 .9c.5 1.2 1.4 2.1 2.6 2.7l.9-1 2.2.8v1.6c0 .5-.5 1-1.1 1C9.6 13.5 6.5 10.4 6 6.6c0-.6.4-1.1 1-1.1z" fill="currentColor"/></symbol>
  <symbol id="i-web" viewBox="0 0 20 20"><circle cx="10" cy="10" r="8.6" fill="none" stroke="currentColor" stroke-width="1.4"/><circle cx="10" cy="10" r="4.4" fill="currentColor"/></symbol>
  <symbol id="i-mail" viewBox="0 0 20 20"><circle cx="10" cy="10" r="8.6" fill="none" stroke="currentColor" stroke-width="1.4"/><rect x="5.5" y="7" width="9" height="6.5" rx=".6" fill="currentColor"/><path d="M5.8 7.4l4.2 3.2 4.2-3.2" fill="none" stroke="var(--card-dark)" stroke-width=".9"/></symbol>
  <symbol id="i-pin" viewBox="0 0 20 20"><circle cx="10" cy="10" r="8.6" fill="none" stroke="currentColor" stroke-width="1.4"/><path d="M10 4.8a3.3 3.3 0 0 0-3.3 3.3c0 2.4 3.3 6.4 3.3 6.4s3.3-4 3.3-6.4A3.3 3.3 0 0 0 10 4.8z" fill="currentColor"/><circle cx="10" cy="8.1" r="1.2" fill="var(--card-dark)"/></symbol>
  <symbol id="i-leaf" viewBox="0 0 10 8"><path d="M1 7C1 3 4 1 9 1 9 5 6 7 1 7z" fill="currentColor"/></symbol>
</svg>

<div class="concept-label" style="top:50px">Concept A</div>
<section class="card card--split card--a" aria-label="Concept A business card">
  <div class="panel-light">
    <div class="brand"><span class="brand-dot"></span>Copper lark</div>
    <ul class="services">
      <li><svg class="leaf" style="color:var(--ink)"><use href="#i-leaf"/></svg>Licenced Builder</li>
      <li><svg class="leaf" style="color:var(--ink)"><use href="#i-leaf"/></svg>Speacial projects</li>
      <li><svg class="leaf" style="color:var(--ink)"><use href="#i-leaf"/></svg>Joiner</li>
      <li><svg class="leaf" style="color:var(--ink)"><use href="#i-leaf"/></svg>New build</li>
    </ul>
    <div class="skyline" role="img" aria-label="Green city skyline silhouette"></div>
  </div>
  <div class="panel-dark">
    <div class="person"><p class="person-name"><span class="initial">M</span>ara <span class="initial">H</span>olt</p><p class="person-role">Directer</p></div>
    <ul class="contacts">
      <li><svg class="contact-icon" style="color:#fff"><use href="#i-phone"/></svg>0400 318 552</li>
      <li><svg class="contact-icon" style="color:#fff"><use href="#i-web"/></svg>www.copperlark.com</li>
      <li><svg class="contact-icon" style="color:#fff"><use href="#i-mail"/></svg>hi@copperlark.com</li>
      <li><svg class="contact-icon" style="color:#fff"><use href="#i-pin"/></svg>18 Tannery Lane.</li>
    </ul>
  </div>
</section>

<div class="concept-label" style="top:430px">Concept B</div>
<section class="card card--split card--b" aria-label="Concept B business card">
  <div class="panel-light">
    <div class="brand"><span class="brand-dot"></span>Copper lark</div>
    <div class="person"><p class="person-name"><span class="initial">M</span>ara <span class="initial">H</span>olt</p><p class="person-role">Directer</p></div>
    <div class="skyline" role="img" aria-label="Green city skyline silhouette"></div>
  </div>
  <div class="panel-dark">
    <ul class="contacts">
      <li><svg class="contact-icon" style="color:#fff"><use href="#i-phone"/></svg>0400 318 552</li>
      <li><svg class="contact-icon" style="color:#fff"><use href="#i-web"/></svg>www.copperlark.com</li>
      <li><svg class="contact-icon" style="color:#fff"><use href="#i-mail"/></svg>hi@copperlark.com</li>
      <li><svg class="contact-icon" style="color:#fff"><use href="#i-pin"/></svg>18 Tannery Lane.</li>
    </ul>
    <ul class="services">
      <li><svg class="leaf" style="color:var(--green-bright)"><use href="#i-leaf"/></svg>Licenced Builder</li>
      <li><svg class="leaf" style="color:var(--green-bright)"><use href="#i-leaf"/></svg>Speacial projects</li>
      <li><svg class="leaf" style="color:var(--green-bright)"><use href="#i-leaf"/></svg>Joiner</li>
      <li><svg class="leaf" style="color:var(--green-bright)"><use href="#i-leaf"/></svg>New build</li>
    </ul>
  </div>
</section>

<div class="concept-label" style="top:812px">Concept C</div>
<section class="card card--c" aria-label="Concept C business card">
  <svg class="diagonals" width="462" height="288" aria-hidden="true">
    <polygon points="320,0 336,0 62,160 40,160" fill="var(--card-dark)"/>
    <polygon points="300,0 306,0 44,150 38,150" fill="var(--stripe-grey)"/>
    <polygon points="0,114 70,150 0,186" fill="var(--green-bright)"/>
  </svg>
  <div class="brand"><span class="brand-dot"></span>Copper lark</div>
  <div class="person"><p class="person-name">Mara Holt</p><p class="person-role">Directer</p></div>
  <ul class="contacts">
    <li><svg class="contact-icon" style="color:var(--ink)"><use href="#i-phone"/></svg>0400 318 552</li>
    <li><svg class="contact-icon" style="color:var(--ink)"><use href="#i-web"/></svg>www.copperlark.com</li>
    <li><svg class="contact-icon" style="color:var(--ink)"><use href="#i-mail"/></svg>hi@copperlark.com</li>
    <li><svg class="contact-icon" style="color:var(--ink)"><use href="#i-pin"/></svg>18 Tannery Lane.</li>
  </ul>
  <div class="skyline" role="img" aria-label="Green city skyline silhouette"></div>
  <div class="footer-strip">
    <ul class="services">
      <li><svg class="leaf" style="color:#fff"><use href="#i-leaf"/></svg>Licenced Builder</li>
      <li><svg class="leaf" style="color:#fff"><use href="#i-leaf"/></svg>Joiner</li>
      <li><svg class="leaf" style="color:#fff"><use href="#i-leaf"/></svg>Speacial projects</li>
      <li><svg class="leaf" style="color:#fff"><use href="#i-leaf"/></svg>New build</li>
    </ul>
  </div>
</section>
</body>
</html>
```